Electrical company business card design.

Hi, were an electrical company in Harrowvale New Zealand called Quarneth Ltd. We focus mainly on high end residential and commercial so the card would be targeted towards that.
The card will be for myself, i am the director of the company.
Name: Derek Olstow
Position: Director/electrician
Phone: 021 387 9415
Email: derek@quarneth.co.nz
Location: Harrowvale
As for colors the the blue color in the logo is preferred, i also don't mind a black background option.
Target Market(s)
High end residential and commercial
Industry/Entity Type
Electrician
Contact Information for Business Card
Name: Derek Olstow Position: Director/Electrician Phone: 021 387 9415, Email: derek@quarneth.co.nz, Location: Harrowvale

```html
<!DOCTYPE html>
<html lang="en">
<head>
<meta charset="utf-8">
<title>Quarneth Ltd – Business Card</title>
<link rel="stylesheet" href="https://fonts.googleapis.com/css2?family=Montserrat:wght@600;700;800&family=Roboto:wght@400&display=swap">
<style>
  :root {
    --canvas-bg: #e4e4e2;
    --card-black: #050505;
    --card-white: #f1f1f1;
    --brand-blue: #1f6fc4;
    --brand-blue-deep: #0a4fa3;
    --brand-grey: #4f5255;
    --logo-grey: #5a5d60;
    --ink: #1b1b1b;
  }
  * { margin: 0; padding: 0; box-sizing: border-box; }
  html, body {
    width: 1200px;
    height: 1000px;
    overflow: hidden;
    background: var(--canvas-bg);
  }
  .canvas {
    position: relative;
    width: 1200px;
    height: 1000px;
  }
  .card {
    position: absolute;
    width: 620px;
    height: 354px;
    border-radius: 4px;
    box-shadow: 0 10px 26px rgba(0, 0, 0, 0.18);
    overflow: hidden;
  }
  .card--back {
    left: 100px;
    top: 90px;
    background: var(--card-black);
  }
  .card--front {
    left: 480px;
    top: 556px;
    background: var(--card-white);
  }
  .wordmark {
    position: absolute;
    left: 0;
    right: 0;
    display: flex;
    align-items: center;
    justify-content: center;
    gap: 14px;
    font-family: "Montserrat", sans-serif;
    font-weight: 600;
    font-size: 46px;
    letter-spacing: 2px;
    color: var(--logo-grey);
  }
  .wordmark__square {
    width: 26px;
    height: 26px;
    background: var(--brand-blue);
  }
  .card--back .wordmark { top: 142px; }
  .card--front .wordmark { top: 58px; font-size: 40px; }
  .card--front .wordmark__square { width: 22px; height: 22px; }

  .identity {
    position: absolute;
    right: 272px;
    top: 196px;
    text-align: right;
    font-family: "Montserrat", sans-serif;
  }
  .identity__name {
    font-weight: 800;
    font-size: 27px;
    letter-spacing: 0.5px;
    color: var(--brand-blue);
    text-transform: uppercase;
    line-height: 1.1;
  }
  .identity__role {
    margin-top: 6px;
    font-weight: 600;
    font-size: 17px;
    letter-spacing: 0.6px;
    color: var(--ink);
    text-transform: uppercase;
  }
  .divider {
    position: absolute;
    left: 368px;
    top: 166px;
    width: 1.5px;
    height: 88px;
    background: var(--brand-blue);
  }
  .contact {
    position: absolute;
    left: 392px;
    top: 172px;
    list-style: none;
    font-family: "Roboto", sans-serif;
    font-size: 18px;
    color: var(--ink);
  }
  .contact__item {
    display: flex;
    align-items: center;
    gap: 10px;
    height: 32px;
  }
  .contact__icon { width: 16px; height: 16px; flex: none; }
  .accent-band {
    position: absolute;
    bottom: 22px;
    height: 7px;
  }
  .accent-band--blue {
    left: 0;
    width: 404px;
    background: linear-gradient(90deg, var(--brand-blue-deep), var(--brand-blue));
  }
  .accent-band--grey {
    left: 408px;
    right: 0;
    background: var(--brand-grey);
  }
</style>
</head>
<body>
<main class="canvas">
  <section class="card card--back" aria-label="Card back">
    <div class="wordmark"><span class="wordmark__square"></span>QUARNETH</div>
  </section>

  <section class="card card--front" aria-label="Card front">
    <div class="wordmark"><span class="wordmark__square"></span>QUARNETH</div>

    <div class="identity">
      <p class="identity__name">Derek Olstow</p>
      <p class="identity__role">Director / Electrician</p>
    </div>

    <div class="divider"></div>

    <ul class="contact">
      <li class="contact__item">
        <svg class="contact__icon" viewBox="0 0 16 16" aria-hidden="true">
          <rect x="1" y="2" width="14" height="13" rx="2" fill="var(--brand-blue)"/>
          <rect x="3" y="4" width="3" height="9" rx="1" fill="#fff"/>
          <rect x="8" y="4" width="5" height="3" fill="#fff"/>
          <circle cx="9" cy="9.5" r="0.9" fill="#fff"/>
          <circle cx="12" cy="9.5" r="0.9" fill="#fff"/>
          <circle cx="9" cy="12" r="0.9" fill="#fff"/>
          <circle cx="12" cy="12" r="0.9" fill="#fff"/>
        </svg>
        <span>021 387 9415</span>
      </li>
      <li class="contact__item">
        <svg class="contact__icon" viewBox="0 0 16 16" aria-hidden="true">
          <path d="M8 1a5 5 0 0 0-5 5c0 4 5 9 5 9s5-5 5-9a5 5 0 0 0-5-5z" fill="var(--brand-blue)"/>
          <circle cx="8" cy="6" r="2" fill="#fff"/>
        </svg>
        <span>Harrowvale</span>
      </li>
    </ul>

    <div class="accent-band accent-band--blue"></div>
    <div class="accent-band accent-band--grey"></div>
  </section>
</main>
</body>
</html>
```